App needs a flyer design

We need a flyer design for my new app called'Vexa books', it is a fast, free and fun way to buy and sell used books. I want to see the following features described on the flyer,my first language is not English so I need designers to thinks how to use short language to describe my APP in a short and eye catching way:
selling a book can't be easier on Vexa Books. Scan the barcode or search for the book, then fill in the price,book condition and your contact information.
To buy a book , you can search for listings in your campus and then contact them. You can trade textbooks with other students in campus,.
U can download from Brenzo Loft and Marvle Spin
You need to put my logo(attached file)n the flyer.

Target Market(s)

Uni students

Industry/Entity Type

Trade

Requirements
Must have
• It's features
Nice to have
• The app page as show in the attachment

```html
<!DOCTYPE html>
<html lang="en">
<head>
<meta charset="utf-8">
<title>Vexa Books – Flyer</title>
<link rel="stylesheet" href="https://fonts.googleapis.com/css2?family=Russo+One&family=Ubuntu:wght@400;500;700&family=Montserrat:wght@700&display=swap">
<style>
  :root {
    --stage: #d6d6d6;
    --blue: #2d4f8e;
    --blue-deep: #1f3f7a;
    --navy: #1c3d78;
    --orange: #f0532e;
    --yellow: #fde74c;
    --white: #ffffff;
    --ink: #111111;
    --price: #e0164f;
    --link: #3a4fb5;
    --muted: #9a9a9a;
  }
  * { box-sizing: border-box; margin: 0; padding: 0; }
  html, body { width: 1200px; height: 1200px; overflow: hidden; }
  body { background: var(--stage); font-family: "Ubuntu", sans-serif; }

  .poster {
    position: absolute; left: 200px; top: 30px;
    width: 800px; height: 1140px;
    background: var(--orange); overflow: hidden;
  }
  .hero-photo {
    position: absolute; left: 0; top: 0; width: 800px; height: 470px;
    background: linear-gradient(180deg, #3a5c9c 0%, #2d4f8e 55%, #2a4a84 100%);
  }
  .wave { position: absolute; left: 0; top: 0; }

  .brand-mark {
    position: absolute; left: 355px; top: 18px; width: 80px; height: 80px;
    background: var(--orange); border-radius: 12px;
  }
  .intro {
    position: absolute; left: 0; width: 800px; top: 102px; text-align: center;
    font-weight: 700; font-size: 31px; color: var(--white); letter-spacing: 1px;
  }
  .app-name {
    position: absolute; left: 0; width: 800px; top: 138px; text-align: center;
    font-family: "Russo One", sans-serif; font-weight: 400; font-size: 60px; color: var(--white);
    letter-spacing: 3px; text-transform: uppercase;
  }
  .tagline {
    position: absolute; left: 41px; top: 300px;
    font-weight: 500; font-size: 26px; line-height: 34px; color: var(--white);
  }
  .tagline .accent { color: var(--orange); }

  .ribbon { position: absolute; right: 0; top: 0; }

  .phone {
    position: absolute; left: 554px; top: 264px; width: 215px; height: 454px;
    background: #121212; border-radius: 32px;
    box-shadow: 0 14px 18px rgba(0,0,0,.3); z-index: 1;
  }
  .phone .speaker { position: absolute; left: 88px; top: 28px; width: 40px; height: 6px; border-radius: 3px; background: #333; }
  .phone .camera { position: absolute; left: 103px; top: 12px; width: 8px; height: 8px; border-radius: 50%; background: #333; }
  .phone .home-key { position: absolute; left: 88px; top: 404px; width: 38px; height: 38px; border-radius: 50%; border: 2px solid #555; }
  .screen {
    position: absolute; left: 16px; top: 62px; width: 185px; height: 328px;
    background: #e9e9e9; overflow: hidden;
  }
  .status-bar { height: 10px; background: var(--orange); color: var(--white); font-size: 6px; text-align: center; line-height: 10px; }
  .search-bar { height: 24px; background: var(--orange); padding: 4px 6px; }
  .search-field { height: 12px; background: var(--white); border-radius: 2px; font-size: 5px; color: var(--muted); padding: 3px 4px; }
  .listing { background: var(--white); margin-bottom: 8px; height: 58px; padding: 7px 6px; position: relative; }
  .listing .title { color: var(--link); font-size: 8px; }
  .listing .author { color: var(--muted); font-size: 6.5px; margin-top: 5px; }
  .listing .date { color: var(--muted); font-size: 5px; margin-top: 6px; }
  .listing .price { position: absolute; right: 6px; top: 22px; color: var(--price); font-size: 10px; }
  .tab-bar {
    position: absolute; left: 0; bottom: 0; width: 185px; height: 30px;
    background: var(--white); display: flex; justify-content: space-around; align-items: center;
  }
  .tab { text-align: center; font-size: 5px; color: var(--muted); }
  .tab .icon { display: block; width: 10px; height: 9px; margin: 0 auto 2px; background: #b5b5b5; border-radius: 2px; }
  .tab.active { color: var(--orange); }
  .tab.active .icon { background: var(--orange); }

  .free-burst { position: absolute; left: 462px; top: 238px; z-index: 2; }

  .section-tag {
    position: absolute; left: 18px; width: 175px; height: 38px; padding-left: 15px;
    background: var(--white); border-radius: 0 19px 19px 0;
    color: var(--orange); font-weight: 500; font-size: 23px; line-height: 38px;
    box-shadow: 2px 2px 0 rgba(0,0,0,.15);
  }
  .sell-tag { top: 536px; }
  .buy-tag { top: 811px; }
  .steps { position: absolute; left: 40px; list-style: none; }
  .steps li {
    position: relative; padding-left: 34px; color: var(--white);
    font-size: 22px; line-height: 30px;
  }
  .steps li::before {
    content: ""; position: absolute; left: 0; top: 5px;
    width: 20px; height: 20px; border-radius: 50%; background: var(--white);
  }
  .sell-steps { top: 599px; }
  .sell-steps li { margin-bottom: 15px; }
  .buy-steps { top: 867px; }
  .buy-steps li { margin-bottom: 18px; }

  .store-band {
    position: absolute; left: 0; top: 1000px; width: 800px; height: 106px;
    background: var(--white);
  }
  .bottom-band { position: absolute; left: 0; top: 1106px; width: 800px; height: 34px; background: var(--blue-deep); }
  .available {
    position: absolute; left: 59px; top: 1036px;
    font-weight: 700; font-size: 28px; color: var(--navy);
  }
  .store-badge {
    position: absolute; top: 1022px; height: 66px; border-radius: 7px;
    background: var(--ink); color: var(--white); padding: 10px 0 0 62px;
    border: 1px solid #777;
  }
  .store-badge .mark { position: absolute; left: 16px; top: 17px; width: 32px; height: 32px; border-radius: 50%; background: var(--white); }
  .store-badge .small { font-size: 10px; letter-spacing: .5px; display: block; }
  .store-badge .name { font-size: 25px; font-weight: 500; line-height: 30px; display: block; }
  .badge-spin { left: 269px; width: 209px; }
  .badge-loft { left: 517px; width: 221px; }
</style>
</head>
<body>
<main class="poster">
  <div class="hero-photo" role="img" aria-label="Students studying at tables in a library with tall bookshelves, tinted blue"></div>

  <svg class="wave" width="800" height="520" viewBox="0 0 800 520" aria-hidden="true">
    <path d="M0 392 Q 330 488 800 394 L800 520 L0 520 Z" fill="var(--white)"/>
    <path d="M0 400 Q 330 496 800 402 L800 520 L0 520 Z" fill="var(--orange)"/>
  </svg>

  <div class="brand-mark" aria-hidden="true"></div>
  <p class="intro">Intorducting</p>
  <h1 class="app-name">Vexa Books</h1>
  <p class="tagline">It is a Fast, Free and Fun<br>way to <span class="accent">buy</span> and <span class="accent">sell</span> used Books</p>

  <svg class="ribbon" width="210" height="200" viewBox="0 0 210 200" aria-label="Download now!">
    <polygon points="0,0 108,0 210,92 210,198" fill="var(--yellow)"/>
    <g transform="translate(128,62) rotate(42)" font-family="Montserrat, sans-serif" font-weight="700" fill="var(--navy)" text-anchor="middle">
      <text x="0" y="-6" font-size="21" letter-spacing="1">DOWNLOAD</text>
      <text x="0" y="20" font-size="21" letter-spacing="1">NOW!</text>
    </g>
  </svg>

  <div class="phone" role="group" aria-label="App home screen showing used book listings">
    <span class="camera"></span><span class="speaker"></span>
    <div class="screen">
      <div class="status-bar">4:21 PM</div>
      <div class="search-bar"><div class="search-field">Title, code, author</div></div>
      <div class="listing"><p class="title">Tales of the Quiet Harbor</p><p class="author">Marlow, Edith</p><p class="date">At February 11, 2015</p><span class="price">$ 58.00</span></div>
      <div class="listing"><p class="title">Tales of the Quiet Harbor</p><p class="author">Marlow, Edith</p><p class="date">At February 7, 2015</p><span class="price">$ 32.00</span></div>
      <div class="listing"><p class="title">Tales of the Quiet Harbor</p><p class="author">Marlow, Edith</p><p class="date">At February 6, 2015</p><span class="price">$ 76.00</span></div>
      <div class="listing"><p class="title">Tales of the Quiet Harbor</p><p class="author">Marlow, Edith</p><p class="date">At February 1, 2015</p><span class="price">$ 14.00</span></div>
      <nav class="tab-bar">
        <span class="tab active"><i class="icon"></i>Home</span>
        <span class="tab"><i class="icon"></i>Sell</span>
        <span class="tab"><i class="icon"></i>Scan</span>
        <span class="tab"><i class="icon"></i>My Ads</span>
      </nav>
    </div>
    <span class="home-key"></span>
  </div>

  <svg class="free-burst" width="150" height="150" viewBox="0 0 160 160" aria-label="It's free!">
    <polygon fill="var(--yellow)" points="80,2 90,30 112,10 112,40 142,28 130,56 158,62 134,80 158,98 130,104 142,132 112,120 112,150 90,130 80,158 70,130 48,150 48,120 18,132 30,104 2,98 26,80 2,62 30,56 18,28 48,40 48,10 70,30"/>
    <g transform="translate(82,82) rotate(-35)" font-family="Ubuntu, sans-serif" font-weight="700" fill="var(--navy)" text-anchor="middle">
      <text x="0" y="-6" font-size="24">It's</text>
      <text x="0" y="20" font-size="26">FREE!</text>
    </g>
  </svg>

  <h2 class="section-tag sell-tag">Selling Book</h2>
  <ul class="steps sell-steps">
    <li>Scan the Barcode or Search for the Book</li>
    <li>Fill in the Price</li>
    <li>Enter Condition &amp; Contact Information</li>
  </ul>

  <h2 class="section-tag buy-tag">Buy Book</h2>
  <ul class="steps buy-steps">
    <li>Search for listings in your Campus</li>
    <li>Contact them</li>
  </ul>

  <div class="store-band"></div>
  <div class="bottom-band"></div>
  <p class="available">Available on :</p>
  <div class="store-badge badge-spin"><i class="mark"></i><span class="small">APP ON</span><span class="name">Marvle Spin</span></div>
  <div class="store-badge badge-loft"><i class="mark"></i><span class="small">Available on the</span><span class="name">Brenzo Loft</span></div>
</main>
</body>
</html>
```